Tarrowby Builders Business Card Design

We require a business Card for a new Building Company called Tarrowby Builders. We are General Builders that specialize in Industrial, Commercial and Domestic building work. We would like to see a design that incorporates Blue ,Red and White as the colour scheme and a design that will highlight a building theme.
(Once this design is achieved will need to incorporate this for the other side of the business which is Tarrowby Joinery )

Industry/Entity Type

Business

Contact Information for Business Card

TARROWBY BUILDERS
17 Wendalee Rd Nuriootpa SA 5355
Mobile 0427390658
Telephone 08 85947316
Marcus Dewhirst
Director / Supervisor

```html
<!DOCTYPE html>
<html lang="en">
<head>
<meta charset="utf-8">
<title>Tarrowby Joinery Business Card</title>
<link rel="stylesheet" href="https://fonts.googleapis.com/css2?family=Open+Sans:wght@400;600;700&display=swap">
<style>
  :root {
    --backdrop: #3a322e;
    --card: #050505;
    --card-edge: #1a1a1a;
    --accent-red: #e0232e;
    --text-light: #e8e8e8;
    --text-grey: #a9a9a9;
    --divider: #8a1a20;
  }
  * { box-sizing: border-box; margin: 0; padding: 0; }
  html, body {
    width: 1200px;
    height: 900px;
    overflow: hidden;
    background: var(--backdrop);
    font-family: "Open Sans", Arial, sans-serif;
  }
  .canvas {
    position: relative;
    width: 1200px;
    height: 900px;
    display: flex;
    align-items: center;
    justify-content: center;
    gap: 60px;
  }
  .card {
    position: relative;
    width: 520px;
    height: 318px;
    background: var(--card);
    border: 1px solid var(--card-edge);
    box-shadow: 0 18px 40px rgba(0,0,0,0.55);
    overflow: hidden;
  }

  /* Contact side */
  .card--contact .brand {
    position: absolute;
    left: 34px;
    top: 140px;
    display: flex;
    align-items: center;
    gap: 12px;
  }
  .brand__mark {
    width: 18px;
    height: 18px;
    background: var(--accent-red);
    flex: none;
  }
  .brand__name {
    color: var(--accent-red);
    font-weight: 400;
    font-size: 19px;
    letter-spacing: 1.5px;
    line-height: 1.15;
    text-transform: uppercase;
  }
  .divider {
    position: absolute;
    left: 226px;
    top: 40px;
    width: 1px;
    height: 238px;
    background: linear-gradient(to bottom, transparent, var(--divider) 20%, var(--divider) 80%, transparent);
  }
  .contact {
    position: absolute;
    left: 244px;
    right: 16px;
    top: 46px;
    color: var(--text-light);
    font-size: 12.5px;
    line-height: 1.4;
    white-space: nowrap;
  }
  .contact__name {
    color: var(--accent-red);
    font-weight: 700;
    font-size: 14px;
  }
  .contact__role { margin-bottom: 18px; }
  .contact__address { margin-bottom: 16px; }
  .contact__line {
    display: flex;
    align-items: center;
    gap: 8px;
  }
  .contact__line--email { font-size: 12px; letter-spacing: -0.1px; }
  .contact__line svg { width: 11px; height: 11px; flex: none; }

  /* Brand side */
  .card--brand .brand {
    position: absolute;
    left: 0;
    right: 0;
    top: 104px;
    display: flex;
    align-items: center;
    justify-content: center;
    gap: 18px;
  }
  .card--brand .brand__mark {
    width: 34px;
    height: 34px;
    background: var(--text-grey);
  }
  .card--brand .brand__name {
    color: var(--text-grey);
    font-size: 30px;
    letter-spacing: 2px;
  }
  .services {
    position: absolute;
    left: 0;
    right: 0;
    top: 210px;
    text-align: center;
    color: var(--text-grey);
    font-size: 12px;
    letter-spacing: 1.2px;
    text-transform: uppercase;
  }
  .services span { margin: 0 6px; }
</style>
</head>
<body>
<main class="canvas">

  <section class="card card--contact" aria-label="Business card contact side">
    <div class="brand">
      <span class="brand__mark" aria-hidden="true"></span>
      <p class="brand__name">Tarrowby<br>Joinery</p>
    </div>
    <div class="divider" aria-hidden="true"></div>
    <div class="contact">
      <p class="contact__name">Marcus Dewhirst</p>
      <p class="contact__role">Director / Supervisor</p>
      <p class="contact__address">17 Wendalee Rd Nuriootpa<br>SA 5355</p>
      <p class="contact__line">
        <svg viewBox="0 0 12 12" aria-hidden="true"><path d="M2.5 1 L4.5 1 L5.2 3.6 L4 4.6 Q5 7 7.4 8 L8.4 6.8 L11 7.5 L11 9.5 Q10.5 11 9 11 Q1 10 1 3 Q1 1.5 2.5 1 Z" fill="var(--accent-red)"/></svg>
        0427390658
      </p>
      <p class="contact__line">
        <svg viewBox="0 0 12 12" aria-hidden="true"><rect x="3" y="0.5" width="6" height="11" rx="1" fill="none" stroke="var(--accent-red)" stroke-width="1.2"/><rect x="5" y="9" width="2" height="1" fill="var(--accent-red)"/></svg>
        08 85947316
      </p>
      <p class="contact__line contact__line--email">
        <svg viewBox="0 0 12 12" aria-hidden="true"><rect x="0.5" y="2" width="11" height="8" fill="var(--accent-red)"/><path d="M0.5 2 L6 6.5 L11.5 2" fill="none" stroke="var(--card)" stroke-width="1"/></svg>
        m.dewhirst@tarrowbybuilders.com.au
      </p>
    </div>
  </section>

  <section class="card card--brand" aria-label="Business card brand side">
    <div class="brand">
      <span class="brand__mark" aria-hidden="true"></span>
      <p class="brand__name">Tarrowby<br>Joinery</p>
    </div>
    <p class="services">Industrial<span>|</span>Commercial<span>|</span>Residential</p>
  </section>

</main>
</body>
</html>
```